Kestrel Signs Facebook Banner Design

Design a facebook banner for a sign company. I would like to have a modern approach to it.

Product Offering:
Signs
Banners
Decals
Commercial Wraps

```html
<!DOCTYPE html>
<html lang="en">
<head>
<meta charset="utf-8">
<title>Kestrel Signs – Facebook Banner</title>
<link rel="stylesheet" href="https://fonts.googleapis.com/css2?family=Kanit:ital,wght@0,500;0,600;0,800;1,400;1,700&family=Poppins:wght@500;600&display=swap">
<style>
  :root {
    --stage: #424242;
    --paper: #fdf0ee;
    --paper-light: #fffaf9;
    --brand-red: #e8323a;
    --ink: #3d3d3f;
    --white: #ffffff;
    --accent-orange: #ffa44a;
    --accent-orange-text: #b8262c;
    --product-blue: #2a5ab8;
    --swatch-pink: #ecc6d3;
  }
  * { box-sizing: border-box; margin: 0; padding: 0; }
  html, body {
    width: 1200px; height: 630px; overflow: hidden;
    background: var(--stage);
  }
  .banner {
    position: absolute; left: 40px; top: 99px;
    width: 1120px; height: 432px;
    background: linear-gradient(90deg, var(--paper-light), var(--paper));
    overflow: hidden;
    font-family: "Kanit", sans-serif;
  }
  .swatch-fan {
    position: absolute; left: 0; top: 180px; width: 230px; height: 252px;
    background: radial-gradient(ellipse at 0% 100%, var(--swatch-pink) 0%, rgba(236,198,211,0.35) 45%, rgba(236,198,211,0) 75%);
    opacity: 0.7;
  }
  .red-panel { position: absolute; inset: 0; width: 100%; height: 100%; }
  .headline {
    position: absolute; left: 50px; top: 46px;
    font-weight: 500; font-size: 33px; letter-spacing: 0.5px;
    color: var(--ink); white-space: nowrap;
  }
  .headline em { font-style: italic; font-weight: 800; color: var(--brand-red); }
  .brand-name {
    position: absolute; left: 60px; top: 112px; width: 420px;
    text-align: center; color: var(--brand-red);
    font-weight: 800; line-height: 0.95; text-transform: uppercase;
  }
  .brand-name .line-1 { display: block; font-size: 68px; letter-spacing: 1px; }
  .brand-name .line-2 { display: block; font-size: 52px; letter-spacing: 3px; }
  .services-title {
    position: absolute; left: 212px; top: 252px;
    font-family: "Poppins", sans-serif; font-weight: 500; font-style: italic;
    font-size: 22px; color: var(--ink);
    padding: 0 4px 4px; border-bottom: 2px solid var(--brand-red);
  }
  .services {
    position: absolute; left: 25px; top: 297px; width: 560px;
    list-style: none; display: flex; flex-wrap: wrap; justify-content: center;
    column-gap: 24px; row-gap: 6px;
  }
  .services li {
    font-style: italic; font-weight: 700; font-size: 32px; line-height: 44px;
    color: var(--ink); text-transform: uppercase; white-space: nowrap;
    display: flex; align-items: center;
  }
  .services li::before {
    content: ""; width: 15px; height: 15px; border-radius: 50%;
    background: var(--brand-red); margin-right: 7px;
  }
  .product-showcase {
    position: absolute; left: 700px; top: 18px; width: 320px; height: 300px;
    background:
      radial-gradient(ellipse at 40% 55%, var(--product-blue) 0%, rgba(42,90,184,0.6) 35%, rgba(42,90,184,0) 60%),
      radial-gradient(ellipse at 75% 35%, rgba(255,255,255,0.85) 0%, rgba(255,255,255,0) 30%),
      radial-gradient(ellipse at 50% 60%, rgba(255,164,74,0.5) 0%, rgba(255,164,74,0) 70%);
  }
  .cta {
    position: absolute; left: 788px; top: 346px; width: 186px; height: 27px;
    border-radius: 14px; background: var(--accent-orange);
    font-family: "Poppins", sans-serif; font-weight: 600; font-size: 15px;
    color: var(--accent-orange-text); text-align: center; line-height: 28px;
    text-transform: uppercase;
  }
  .contact {
    position: absolute; top: 383px; display: flex; align-items: center; gap: 5px;
    color: var(--white); font-family: "Poppins", sans-serif; white-space: nowrap;
  }
  .contact-phone { left: 676px; font-size: 21px; font-weight: 600; }
  .contact-web { left: 868px; font-size: 17px; font-weight: 500; }
  .contact svg { display: block; }
</style>
</head>
<body>
  <section class="banner">
    <div class="swatch-fan" role="img" aria-label="Faded fan of colour swatch cards"></div>

    <svg class="red-panel" viewBox="0 0 1120 432" aria-hidden="true">
      <defs>
        <filter id="tear-shadow" x="-10%" y="-10%" width="120%" height="120%">
          <feDropShadow dx="-4" dy="0" stdDeviation="5" flood-opacity="0.3"/>
        </filter>
      </defs>
      <polygon filter="url(#tear-shadow)" fill="#e8323a"
        points="635,0 640,8 632,22 628,36 618,48 606,62 600,78 593,96 598,110 588,124 596,140 600,158 594,172 604,188 608,202 616,216 622,232 630,240 618,252 614,268 604,282 610,298 602,312 600,328 607,342 610,358 602,372 598,386 590,400 594,414 582,426 580,432 1120,432 1120,0"/>
    </svg>

    <h1 class="headline">ELEVATE YOUR <em>BUSINESS</em> WITH</h1>

    <div class="brand-name">
      <span class="line-1">Kestrel</span>
      <span class="line-2">Signs</span>
    </div>

    <h2 class="services-title">Our services</h2>
    <ul class="services">
      <li>Signs</li>
      <li>Banners</li>
      <li>Decals</li>
      <li>Commercial Wraps</li>
    </ul>

    <div class="product-showcase" role="img" aria-label="Branded blue water bottle and white mug with colourful paint splashes"></div>

    <div class="cta">Contact us today</div>

    <div class="contact contact-phone">
      <svg width="18" height="18" viewBox="0 0 24 24" aria-hidden="true">
        <path fill="#ffffff" d="M6.6 10.8c1.4 2.8 3.8 5.1 6.6 6.6l2.2-2.2c.3-.3.7-.4 1-.2 1.1.4 2.3.6 3.6.6.6 0 1 .4 1 1V20c0 .6-.4 1-1 1C10.6 21 3 13.4 3 4c0-.6.4-1 1-1h3.5c.6 0 1 .4 1 1 0 1.3.2 2.5.6 3.6.1.3 0 .7-.2 1L6.6 10.8z"/>
      </svg>
      <span>(555) 014-2290</span>
    </div>

    <div class="contact contact-web">
      <svg width="17" height="17" viewBox="0 0 24 24" aria-hidden="true" fill="none" stroke="#ffffff" stroke-width="1.6">
        <circle cx="12" cy="12" r="10"/>
        <ellipse cx="12" cy="12" rx="4.5" ry="10"/>
        <line x1="2" y1="12" x2="22" y2="12"/>
        <path d="M4 7h16M4 17h16"/>
      </svg>
      <span>www.kestrelsigns.ca</span>
    </div>
  </section>
</body>
</html>
```